business cards for Tramvex
Tramvexa
business cards for Tramvex - Government
Modern
R.K.Dunmore
914 E Harlan Avenue, Suite 215 Fort Worth, TX 76102
rdunmore@tramvexa-mail.com
www.tramvexa-site.com
need to be able to create cards for other people- the backside is logo only- the front needs my name then tramvexa with address email phone number and website- please put logo on front side as well. colors can be red/white/blue/ black or any combination
big version of logo and possibly ability to write on it- this may not work out well so if it doesn't then don't do it.

```html
<!DOCTYPE html>
<html lang="en">
<head>
<meta charset="utf-8">
<title>Tramvexa business cards</title>
<link href="https://fonts.googleapis.com/css2?family=Questrial&display=swap" rel="stylesheet">
<style>
  :root {
    --bg: #e6e4e1;
    --card: #ffffff;
    --navy: #1f3466;
    --red: #b3202a;
    --ink: #3a3a3a;
    --rule: #8a8a8a;
  }
  html, body {
    margin: 0;
    padding: 0;
    width: 1200px;
    height: 901px;
    overflow: hidden;
    background: var(--bg);
    font-family: "Questrial", "Century Gothic", sans-serif;
  }
  .canvas { position: relative; width: 1200px; height: 901px; }
  .card {
    position: absolute;
    width: 540px;
    height: 310px;
    background: var(--card);
    border-radius: 14px;
    box-shadow: 0 6px 18px rgba(0,0,0,0.18);
  }
  .card-back { left: 60px; top: 130px; }
  .card-front { left: 600px; top: 460px; }

  .brand { display: flex; align-items: center; gap: 12px; color: var(--navy); }
  .brand-mark { display: block; background: var(--navy); }
  .brand-name { font-weight: 400; letter-spacing: 1px; }

  .card-back .brand { position: absolute; left: 0; right: 0; top: 108px; justify-content: center; }
  .card-back .brand-mark { width: 44px; height: 44px; }
  .card-back .brand-name { font-size: 40px; }
  .card-back .website {
    position: absolute; left: 0; right: 0; bottom: 58px;
    text-align: center; font-size: 12px; letter-spacing: 3px; color: var(--ink);
  }

  .card-front .brand { position: absolute; left: 230px; top: 66px; }
  .card-front .brand-mark { width: 30px; height: 30px; }
  .card-front .brand-name { font-size: 30px; }

  .holder {
    position: absolute; left: 52px; top: 186px;
    color: var(--red); font-size: 17px; letter-spacing: 0.5px;
  }
  .divider {
    position: absolute; left: 250px; top: 160px;
    width: 1px; height: 108px; background: var(--rule);
  }
  .contact {
    position: absolute; left: 272px; top: 160px;
    font-size: 13px; line-height: 18px; color: var(--ink);
  }
  .contact p { margin: 0; }
  .contact .row { display: flex; align-items: center; gap: 8px; }
  .contact .address { margin-bottom: 4px; }
  .icon { width: 12px; height: 12px; fill: var(--navy); flex: none; }
</style>
</head>
<body>
<div class="canvas">

  <section class="card card-back">
    <div class="brand">
      <span class="brand-mark"></span>
      <span class="brand-name">Tramvexa</span>
    </div>
    <p class="website">www.tramvexa-site.com</p>
  </section>

  <section class="card card-front">
    <div class="brand">
      <span class="brand-mark"></span>
      <span class="brand-name">Tramvexa</span>
    </div>

    <p class="holder">R.K.Dunmore</p>
    <span class="divider"></span>

    <div class="contact">
      <div class="address">
        <p>914 E Harlan Avenue, Suite 215</p>
        <p>Fort Worth, TX 76102</p>
      </div>
      <p class="row">
        <svg class="icon" viewBox="0 0 24 24"><path d="M6.6 10.8a15.1 15.1 0 0 0 6.6 6.6l2.2-2.2a1 1 0 0 1 1-.25 11.4 11.4 0 0 0 3.6.57 1 1 0 0 1 1 1V20a1 1 0 0 1-1 1A17 17 0 0 1 3 4a1 1 0 0 1 1-1h3.5a1 1 0 0 1 1 1c0 1.25.2 2.45.57 3.6a1 1 0 0 1-.25 1z"/></svg>
        817.555.0148
      </p>
      <p class="row">
        <svg class="icon" viewBox="0 0 24 24"><path d="M2 5h20v14H2z M3.5 6.5 12 13l8.5-6.5" fill="none" stroke="#1f3466" stroke-width="2"/></svg>
        rdunmore@tramvexa-mail.com
      </p>
      <p class="row">
        <svg class="icon" viewBox="0 0 24 24"><circle cx="12" cy="12" r="9.5" fill="none" stroke="#1f3466" stroke-width="2"/><path d="M2.5 12h19M12 2.5c3 3 3 16 0 19M12 2.5c-3 3-3 16 0 19" fill="none" stroke="#1f3466" stroke-width="1.6"/></svg>
        www.tramvexa-site.com
      </p>
    </div>
  </section>

</div>
</body>
</html>
```